Webbanner-Design für Fachhandel für Medizinprodukte
Zielgruppe
wir sind ein Fachhandel für Medizinprodukte.
Aufgabenstellung
-Slider / Banner
-1920 x 340
-Es muss ein intersannter Satz auf dem Bild sein, der einläd zu klicken.
-https://www.veloquar-beispiel.de/
- folgender Artikel soll beworben werden:
-https://www.veloquar-beispiel.de/fingerpulsoximeter-kt508-pulsoximeter-weiss-4186
-Design soll gut zur Seite passen.
-Das Bild kann von der Seite verwendet werden.
-Gerne können zusätzlich auch Stockbilder verarbeitet werden.

```html
<!DOCTYPE html>
<html lang="de">
<head>
<meta charset="utf-8">
<title>VELOQUAR – Fingerpulsoximeter KT508</title>
<link rel="stylesheet" href="https://fonts.googleapis.com/css2?family=Montserrat:ital,wght@0,700;0,800;1,800&display=swap">
<style>
  :root {
    --page-bg: #e0e0de;
    --banner-bg: #efefef;
    --brand-green: #43ae4a;
    --tag-orange: #f0921e;
    --white: #ffffff;
    --ink: #3a3d3f;
    --product-light: #f7f7f7;
    --product-shade: #d9dadb;
  }
  * { box-sizing: border-box; margin: 0; padding: 0; }
  html, body {
    width: 1200px;
    height: 494px;
    overflow: hidden;
    background: var(--page-bg);
    font-family: "Montserrat", Arial, sans-serif;
  }
  .banner {
    position: absolute;
    left: 90px;
    top: 156px;
    width: 1021px;
    height: 181px;
    background: var(--banner-bg);
    overflow: hidden;
  }
  .banner__band {
    position: absolute;
    inset: 0;
    width: 100%;
    height: 100%;
  }
  .product-visual {
    position: absolute;
    left: 47px;
    top: 16px;
    width: 225px;
    height: 141px;
    border-radius: 14px;
    background: linear-gradient(135deg, var(--product-light), var(--product-shade));
  }
  .model-tag {
    position: absolute;
    left: 141px;
    top: 32px;
    width: 134px;
    height: 31px;
    background: var(--tag-orange);
    color: var(--white);
    font-weight: 800;
    font-size: 21px;
    line-height: 31px;
    text-align: center;
    letter-spacing: 0.5px;
  }
  .headline {
    position: absolute;
    left: 268px;
    width: 500px;
    top: 18px;
    color: var(--white);
    font-weight: 800;
    font-style: italic;
    font-size: 60px;
    line-height: 66px;
    text-align: center;
    text-transform: uppercase;
    white-space: nowrap;
  }
  .brand {
    position: absolute;
    left: 825px;
    top: 30px;
    width: 166px;
    text-align: center;
    color: var(--ink);
    font-weight: 800;
    font-size: 22px;
    line-height: 1;
    letter-spacing: 0.5px;
  }
  .cta {
    position: absolute;
    left: 806px;
    top: 109px;
    width: 184px;
    height: 48px;
    border-radius: 8px;
    background: var(--brand-green);
    color: var(--white);
    font-weight: 700;
    font-size: 15px;
    line-height: 48px;
    text-align: center;
    text-decoration: none;
    box-shadow: 0 3px 8px rgba(0, 0, 0, 0.12);
  }
</style>
</head>
<body>
  <section class="banner" aria-label="Fingerpulsoximeter KT508">
    <svg class="banner__band" viewBox="0 0 1021 181" preserveAspectRatio="none" aria-hidden="true">
      <polygon points="232,0 793,0 765,181 206,181" fill="var(--brand-green)"/>
    </svg>
    <div class="product-visual" role="img" aria-label="Produktfoto: zwei weiße Fingerpulsoximeter mit Digitalanzeige"></div>
    <div class="model-tag">KT508</div>
    <h1 class="headline">Schnell<br>&amp; Genaue</h1>
    <div class="brand">VELOQUAR</div>
    <a class="cta" href="https://www.veloquar-beispiel.de/fingerpulsoximeter-kt508-pulsoximeter-weiss-4186">Jetzt Einkaufen</a>
  </section>
</body>
</html>
```